KD Group Company brochure

require the design of a brochure for my company KD group which incorporates 2 separate companies specialising in home technology and security. Im not sure whether its going to be best to do one brochure with all the info in or 2 individual ones

Target Market(s)

Footballers and High net worth individuals

Industry/Entity Type

Information Technology

Font styles to use
Serif
Other font styles liked:
• Neuropol (this is the logo font)

Colors
ec1f27
000000
9d9d9d

Requirements
Must have
• 2 sections one for audio visual and 1 for security

```html
<!DOCTYPE html>
<html lang="en">
<head>
<meta charset="utf-8">
<title>Halden Technologies Brochure</title>
<link rel="stylesheet" href="https://fonts.googleapis.com/css2?family=Orbitron:wght@500&family=Ubuntu:wght@400;500&display=swap">
<style>
  :root {
    --red: #ec1f27;
    --black: #000000;
    --ink: #0c0c0c;
    --grey: #9d9d9d;
    --panel: #ececec;
    --stage: #d6d6d6;
    --white: #ffffff;
  }
  * { box-sizing: border-box; margin: 0; padding: 0; }
  html, body { width: 1062px; height: 1200px; overflow: hidden; }
  body {
    background: var(--stage);
    font-family: "Ubuntu", sans-serif;
    position: relative;
  }
  .spread {
    position: absolute;
    left: 51px;
    width: 960px;
    height: 480px;
    display: flex;
    box-shadow: 0 8px 24px rgba(0,0,0,.25);
  }
  .spread--intro { top: 60px; }
  .spread--features { top: 660px; }
  .page {
    width: 480px;
    height: 480px;
    background: var(--black);
    position: relative;
    padding: 18px;
    overflow: hidden;
  }
  .page--left { border-right: 1px solid #222; }

  /* Intro page */
  .intro { padding: 42px 48px 36px; color: var(--white); }
  .brand {
    display: flex; flex-direction: column; align-items: center;
    margin-bottom: 22px;
  }
  .brand__mark {
    width: 30px; height: 30px; border-radius: 50%;
    background: var(--grey); margin-bottom: 6px;
  }
  .brand__name {
    font-family: "Ubuntu", sans-serif; font-weight: 500;
    font-size: 16px; letter-spacing: 1px; color: var(--grey);
    text-align: center; line-height: 1.1;
  }
  .intro p {
    font-size: 9px; line-height: 1.5; margin-bottom: 8px;
    text-align: justify; color: #eaeaea;
  }
  .intro p:last-child { margin-bottom: 0; }

  /* Feature pages */
  .photos {
    height: 272px; display: grid; gap: 4px;
  }
  .photos--av { grid-template-columns: 110px 1fr; grid-template-rows: 1fr 1fr 1fr; }
  .photos--av .ph-main { grid-column: 2; grid-row: 1 / 4; }
  .photos--cinema { grid-template-columns: 1fr 1fr; grid-template-rows: 1fr 1fr; }
  .photos--cinema .ph-main { grid-column: 1; grid-row: 1 / 3; }
  .photos--lighting { grid-template-columns: 1fr 1fr; grid-template-rows: 1fr 1fr; }
  .photos--lighting .ph-main { grid-column: 2; grid-row: 1 / 3; }
  .ph { width: 100%; height: 100%; }
  .ph--room-warm { background: linear-gradient(135deg, #8a6a4e, #3d2c22); }
  .ph--room-light { background: linear-gradient(160deg, #e6e1d8, #9a8f80); }
  .ph--hall { background: linear-gradient(180deg, #b9b2a6, #4c4842); }
  .ph--office { background: linear-gradient(160deg, #d9d4cc, #8b8378); }
  .ph--cinema-dark { background: linear-gradient(160deg, #4a4a52, #2a2028); }
  .ph--cinema-screen { background: linear-gradient(180deg, #3a5e92, #2a1822); }
  .ph--cinema-purple { background: linear-gradient(180deg, #5a4a8a, #3a2a22); }
  .ph--lounge-blue { background: linear-gradient(160deg, #3a3ea0, #6a4aa8); }
  .ph--house-night { background: linear-gradient(180deg, #1e2a52, #4a5030); }
  .ph--pool { background: linear-gradient(180deg, #6a1e1e 0%, #2a8ac8 50%, #c8a8a0 100%); }

  .panel {
    background: var(--panel);
    height: 170px;
    margin-top: 2px;
    padding: 28px 26px 20px;
    overflow: hidden;
  }
  .panel__title {
    font-family: "Orbitron", sans-serif; font-weight: 500;
    font-size: 19px; color: var(--ink); margin-bottom: 12px;
  }
  .panel__title em { font-style: normal; color: var(--red); }
  .panel ul { list-style: disc; padding-left: 14px; }
  .panel li { font-size: 9.6px; line-height: 1.55; color: #222; }
</style>
</head>
<body>

<section class="spread spread--intro">
  <article class="page page--left intro">
    <div class="brand">
      <span class="brand__mark"></span>
      <span class="brand__name">HALDEN<br>technologies</span>
    </div>
    <p>Halden Technologies provide an extensive range of state-of-the-art video conferencing and audio visual services, combining design, procurement, implementation and support to give a complete end to end service.</p>
    <p>Our highly trained staff provide a focused approach to the design and installation of control, visual and audio systems. Project managers and engineers are highly experienced in a wide range of services involving multi-room, multi-source audio visual systems, lighting and video conferencing, thus providing a complete suite of professionally installed solutions.</p>
    <p>Our services include video conferencing to single user, desktop or multi room environments; Integrated Audio Visual to commercial, home &amp; marine sectors; Interactive Audio Visual providing true collaboration anytime, anywhere; Audio Visual Control for intuitive operation of all equipment and management of systems locally or over the WAN to include lighting, blinds and thermostat control; Digital Signage providing a replacement solution for static signs communicating key information and complex messages to almost any audience, anytime, anywhere; Distributed TV and Video including High Definition feeds to any device using the structured data cabling network.</p>
    <p>Our designs combine a simple approach of understanding a client's functional requirements within a space, consideration of the complete IT infrastructure and then matching these needs to a design that gives maximum user experience, intuitive control, sustainability and provide a value for money on your investment.</p>
  </article>

  <article class="page page--right">
    <div class="photos photos--av">
      <div class="ph ph--room-light" role="img" aria-label="Bright living room with wall-mounted screen"></div>
      <div class="ph ph--hall" role="img" aria-label="Hallway with glass floor panel"></div>
      <div class="ph ph--office" role="img" aria-label="Open-plan office with display"></div>
      <div class="ph ph--room-warm ph-main" role="img" aria-label="Study with built-in television, shelving and pendant light"></div>
    </div>
    <div class="panel">
      <h2 class="panel__title">Audio Visual <em>Systems</em></h2>
      <ul>
        <li>Easy, discreet access to all your music, wherever you are in your home or garden</li>
        <li>Tunebox, Streamly, Internet Radio, DAB etc all supported</li>
        <li>Full HD TV and direct access to your personal TV recordings wherever you are in the house</li>
        <li>We're committed to the highest quality music and images - even old school Hi-Fi buffs can get what they need from our team</li>
      </ul>
    </div>
  </article>
</section>

<section class="spread spread--features">
  <article class="page page--left">
    <div class="photos photos--cinema">
      <div class="ph ph--cinema-dark ph-main" role="img" aria-label="Home cinema room with sofa and wall screen"></div>
      <div class="ph ph--cinema-screen" role="img" aria-label="Tiered cinema seating facing a projection screen"></div>
      <div class="ph ph--cinema-purple" role="img" aria-label="Cinema room with purple lighting and armchairs"></div>
    </div>
    <div class="panel">
      <h2 class="panel__title">Home <em>Cinema</em></h2>
      <ul>
        <li>Professionally designed home cinema – tailored to suit your budget and your space</li>
        <li>We can deliver dedicated projection screening rooms with sound and images equalling commercial cinemas or discreet solutions that disappear when they're not needed</li>
        <li>Who will love this more-you or your kids?</li>
      </ul>
    </div>
  </article>

  <article class="page page--right">
    <div class="photos photos--lighting">
      <div class="ph ph--lounge-blue" role="img" aria-label="Lounge with blue mood lighting"></div>
      <div class="ph ph--house-night" role="img" aria-label="House exterior lit at night"></div>
      <div class="ph ph--pool ph-main" role="img" aria-label="Indoor pool with chequered floor and arches"></div>
    </div>
    <div class="panel">
      <h2 class="panel__title">Lighting Control <em>&amp; Design</em></h2>
      <ul>
        <li>Mood lighting – whole room or house control from a single button press</li>
        <li>Energy efficient lighting</li>
        <li>Automated window treatments from world leading manufacturer Lumivane</li>
        <li>Full automation giving control and timer functions when you are away from home</li>
      </ul>
    </div>
  </article>
</section>

</body>
</html>
```